Custom beer tap decals, Calloway Alehouse, Tasmania, Australia.

UPDATE 22/6/2017

Based on designs received so far, Im after more of a bold/clean design. This must standout. See attached example.

Beer tap decals for 4 different products. Rustic/English feel, with some modern vibrancy, maintain original branding as much as possible.
The size bust be a 95mm circle. Please see attached artwork.
The same branding theme must carry across all four designs. While each can be different, the core branding remaining the same is important.
Happy for different fonts to be used, but they must be clearly readable. The font for the 'Calloway Alehouse' component must remain the same.
The colours used in the flag banner part of the decal must remain the same as these reflect the colours on our bottle labels.

Highlighting the 'Made in Tasmania' component would be nice, although not entirely necessary.

Plus a 'Limited Release; design including white space where one off beers can be written in permanent marker, we brew quite a few small batch beers per year and it doesn’t make sense to have custom decals for each. Having a generic limited release decal that we can change ourselves would be a big help.

Target Market(s)

Graphic design, beer, brewery.

Industry/Entity Type

Brewery

Colors

Designer to choose colors to be used in the design.

Requirements
Must have
• 'Calloway Alehouse' component of supplied decals must remain. Would be nice to incorporate some of the shield elements, but isn't vital.
Nice to have
• Rustic/earth themes, with a modern twist and vibrance.

```html
<!DOCTYPE html>
<html lang="en">
<head>
<meta charset="utf-8">
<title>Calloway Alehouse – Irish Red Ale tap decal</title>
<link rel="stylesheet" href="https://fonts.googleapis.com/css2?family=Cinzel:wght@900&family=Almendra:wght@700&family=Uncial+Antiqua&family=Bungee+Inline&display=swap">
<style>
  :root {
    --bg: #ffffff;
    --shield-black: #161616;
    --shield-cream: #d8d29a;
    --shield-green: #37461c;
    --shield-maroon: #6a0a0a;
    --field-light: #c6c08e;
    --field-mid: #8f8a62;
    --ink: #111111;
    --cream-text: #f3efcf;
    --banner-red: #863134;
    --ribbon-light: #6e6a52;
    --ribbon-dark: #2f2d22;
    --leaf-green: #2f9a22;
    --leaf-light: #5fcf48;
  }
  html, body {
    margin: 0;
    padding: 0;
    width: 1200px;
    height: 1200px;
    overflow: hidden;
    background: var(--bg);
  }
  .decal {
    display: block;
    width: 1200px;
    height: 1200px;
  }
  .brand-name {
    font-family: "Cinzel", serif;
    font-weight: 900;
    font-size: 178px;
    fill: var(--ink);
    stroke: var(--shield-cream);
    stroke-width: 2;
    letter-spacing: 2px;
  }
  .brand-sub {
    font-family: "Almendra", serif;
    font-weight: 700;
    font-size: 92px;
    fill: var(--ink);
  }
  .tagline {
    font-family: "Uncial Antiqua", serif;
    fill: var(--cream-text);
  }
  .tagline-small { font-size: 58px; }
  .tagline-large { font-size: 54px; }
  .beer-name {
    font-family: "Bungee Inline", sans-serif;
    font-size: 124px;
    fill: var(--ink);
  }
</style>
</head>
<body>
<svg class="decal" viewBox="0 0 1500 1500" xmlns="http://www.w3.org/2000/svg">
  <defs>
    <path id="shield" d="M200,0 L750,0 L1300,0 C1440,230 1500,480 1490,700 C1480,1100 1150,1400 750,1490 C350,1400 20,1100 10,700 C0,480 60,230 200,0 Z"/>
    <radialGradient id="fieldGlow" cx="50%" cy="45%" r="60%">
      <stop offset="55%" stop-color="var(--field-mid)"/>
      <stop offset="100%" stop-color="var(--field-light)"/>
    </radialGradient>
    <linearGradient id="ribbonShade" x1="0" y1="0" x2="0" y2="1">
      <stop offset="0%" stop-color="var(--ribbon-dark)"/>
      <stop offset="50%" stop-color="var(--ribbon-light)"/>
      <stop offset="100%" stop-color="var(--ribbon-dark)"/>
    </linearGradient>
    <radialGradient id="ornamentGlow" cx="50%" cy="50%" r="50%">
      <stop offset="0%" stop-color="var(--leaf-light)" stop-opacity="0.85"/>
      <stop offset="55%" stop-color="var(--leaf-green)" stop-opacity="0.55"/>
      <stop offset="100%" stop-color="var(--leaf-green)" stop-opacity="0"/>
    </radialGradient>
    <filter id="softShadow" x="-10%" y="-10%" width="120%" height="130%">
      <feDropShadow dx="6" dy="10" stdDeviation="6" flood-color="#000" flood-opacity="0.45"/>
    </filter>
  </defs>

  <g class="shield">
    <use href="#shield" fill="var(--shield-black)"/>
    <use href="#shield" fill="var(--shield-cream)" transform="translate(750,760) scale(0.935) translate(-750,-760)"/>
    <use href="#shield" fill="var(--shield-green)" transform="translate(750,770) scale(0.895) translate(-750,-770)"/>
    <use href="#shield" fill="var(--shield-cream)" transform="translate(750,772) scale(0.88) translate(-750,-772)"/>
    <use href="#shield" fill="var(--shield-maroon)" transform="translate(750,775) scale(0.87) translate(-750,-775)"/>
    <use href="#shield" fill="url(#fieldGlow)" transform="translate(750,780) scale(0.855) translate(-750,-780)"/>
  </g>

  <g class="wordmark" text-anchor="middle">
    <text class="brand-name" x="752" y="350" filter="url(#softShadow)" textLength="990" lengthAdjust="spacingAndGlyphs">CALLOWAY</text>
    <text class="brand-sub" x="752" y="490" filter="url(#softShadow)">Alehouse</text>
    <text class="tagline tagline-small" x="740" y="610" filter="url(#softShadow)">Proudly</text>
    <text class="tagline tagline-large" x="742" y="698" filter="url(#softShadow)" textLength="565" lengthAdjust="spacingAndGlyphs">TASMANIAN MADE</text>
    <text class="tagline tagline-small" x="742" y="790" filter="url(#softShadow)">5.1%</text>
  </g>

  <g class="flag-banner" filter="url(#softShadow)">
    <polygon class="ribbon-tail" points="0,885 310,885 310,1092 0,1092 95,988" fill="url(#ribbonShade)"/>
    <polygon class="ribbon-tail" points="1500,885 1190,885 1190,1092 1500,1092 1405,988" fill="url(#ribbonShade)"/>
    <polygon class="banner-front" points="245,845 1210,845 1150,992 1210,1140 245,1140 305,992" fill="var(--banner-red)"/>
  </g>
  <g class="beer-title" text-anchor="middle">
    <text class="beer-name" x="742" y="962" textLength="465" lengthAdjust="spacingAndGlyphs">IRISH RED</text>
    <text class="beer-name" x="742" y="1112" textLength="185" lengthAdjust="spacingAndGlyphs">ALE</text>
  </g>

  <ellipse class="ornament" role="img" aria-label="Green leafy scroll ornament, lower left" cx="230" cy="1345" rx="230" ry="145" fill="url(#ornamentGlow)"/>
  <ellipse class="ornament" role="img" aria-label="Green leafy scroll ornament, lower right" cx="1270" cy="1345" rx="230" ry="145" fill="url(#ornamentGlow)"/>
</svg>
</body>
</html>
```